Brimvale OralNet IT Inc. new website

i need a website for my company which is dedicated to installation and service of computer systems in Dental Offices. I would like for it to encompass a technology feel and professional look. The company deals with all aspects of technology like, Audio Visual, computer systems and networks, Cloud services like data backup, data center. We provide manage services, support and services to Dental Professionals.

Looking for a Technology font but professional look Added Wednesday, April 20, 2016

Target Market(s)

Dental, Dentist

Industry/Entity Type

Dental

Number of Pages Required

5+ page

Font styles to use
Other font styles liked:
• Futuristic or Techy

Colors
0255a3
ec1f27

Requirements
Must have
• Tabs
Nice to have
• Have no idea maybe some suggestion on your part may help
Should not have
• A professional feel but have a techy look

```html
<!DOCTYPE html>
<html lang="en">
<head>
<meta charset="utf-8">
<title>Brimvale OralNet IT Inc. – Technology for Dental Offices</title>
<link href="https://fonts.googleapis.com/css2?family=Exo+2:wght@400;500;600&family=Open+Sans:wght@300;400;600&display=swap" rel="stylesheet">
<style>
:root{
  --navy:#0255a3;
  --blue:#1a8fd8;
  --red:#ec1f27;
  --cyan:#22b3e4;
  --teal:#2fc7c9;
  --panel-a:#0a6fbf;
  --panel-b:#1a8fd8;
  --panel-c:#0255a3;
  --ink:#2f3742;
  --muted:#8a8f95;
  --line:#e6e8ea;
  --soft:#f5f7f9;
  --foot:#1f2f45;
  --foot-text:#a9b6c6;
  --foot-line:#33455e;
}
*{box-sizing:border-box;margin:0;padding:0}
html,body{width:960px;height:1200px;overflow:hidden;background:#fff}
body{font-family:"Open Sans",Arial,sans-serif;color:var(--ink);position:relative}
.abs{position:absolute}
.tech{font-family:"Exo 2","Open Sans",sans-serif}

/* top bar */
.topbar{left:133px;top:0;width:705px;height:18px;border-bottom:1px solid var(--line)}
.topbar .info-line{position:absolute;left:107px;top:4px;display:flex;align-items:center;gap:4px;font-size:6px;color:#555}
.topbar .info-line svg{flex:none}
.topbar .info-line .gap{width:14px}
.topbar .socials{position:absolute;right:107px;top:6px;display:flex;gap:5px}
.topbar .socials i{width:6px;height:6px;border-radius:50%;background:#c4c8cc;display:block}

/* header */
.brand{left:246px;top:29px;font-size:20px;font-weight:600;color:var(--navy);display:flex;align-items:center;gap:7px;letter-spacing:.2px}
.brand i{width:14px;height:14px;background:var(--navy);display:block;border-radius:2px}
.call{left:598px;top:37px;font-size:8.5px;color:#444;display:flex;align-items:center;gap:4px}
.header-rule{left:133px;top:70px;width:705px;height:1px;background:var(--line)}

/* tabbed navigation */
.tabs{left:240px;top:71px;display:flex;font-size:7.5px;color:#333}
.tabs .tab{padding:6px 10px 7px;border-top:2px solid transparent}
.tabs .tab:first-child{padding-left:0}
.tabs .tab.on{color:var(--navy);border-top-color:var(--red);font-weight:600}

/* hero */
.hero{left:133px;top:93px;width:705px;height:198px;background:linear-gradient(90deg,#0255a3 0%,#0d7bcb 40%,#1ea6de 70%,#2fc7c9 100%);overflow:hidden}
.hero .grid-lines{position:absolute;inset:0;background-image:linear-gradient(rgba(255,255,255,.06) 1px,transparent 1px),linear-gradient(90deg,rgba(255,255,255,.06) 1px,transparent 1px);background-size:22px 22px}
.hero-visual{left:560px;top:93px;width:200px;height:198px;background:radial-gradient(ellipse at 50% 50%,rgba(255,255,255,.28) 0%,rgba(255,255,255,.08) 50%,rgba(255,255,255,0) 72%)}
.hero-copy{left:270px;top:124px;color:#fff}
.hero-copy .kicker{font-size:11px;font-weight:300}
.hero-copy .hl{display:inline-block;background:rgba(255,255,255,.2);font-size:16.5px;font-weight:600;padding:1px 6px;margin-top:5px;line-height:21px}
.hero-copy p{font-size:6.3px;line-height:10px;margin-top:15px}
.btns{margin-top:10px;display:flex;gap:6px}
.btn{font-size:5.5px;height:13px;line-height:11px;padding:0 10px;border:1px solid #fff;border-radius:7px;color:#fff}
.btn.fill{background:var(--red);border-color:var(--red)}

/* features */
.feature{top:302px;width:112px;text-align:center}
.feature svg{display:block;margin:0 auto}
.feature h3{font-size:11.5px;font-weight:500;margin-top:18px;color:#333}
.feature p{font-size:6.3px;line-height:10px;color:var(--muted);margin-top:9px;padding:0 4px}

/* info strip */
.info{left:240px;top:430px;width:493px;height:143px;display:flex;color:#fff}
.info>div{padding:16px}
.info h4{font-size:12px;font-weight:500;margin-bottom:17px;position:relative}
.info h4:after{content:"";position:absolute;left:0;bottom:-6px;width:18px;height:2px;background:var(--red)}
.news{width:124px;background:var(--panel-a);font-size:6.3px;line-height:10px}
.hours{width:123px;background:var(--panel-b);font-size:6.2px}
.hours .row{display:flex;justify-content:space-between;padding:0 0 8px;border-bottom:1px solid rgba(255,255,255,.25);margin-bottom:8px}
.book{flex:1;background:var(--panel-c)}
.form{display:grid;grid-template-columns:102px 102px;gap:10px 9px}
.field{height:17px;border:1px solid rgba(255,255,255,.45);border-radius:9px;font-size:6px;line-height:15px;padding-left:10px;color:rgba(255,255,255,.75)}
.field.sel{color:#fff;background:rgba(255,255,255,.08)}
.send{height:17px;border-radius:9px;background:var(--red);color:#fff;font-size:6.3px;line-height:17px;text-align:center;font-weight:600}

/* services */
.services{left:133px;top:583px;width:705px;height:227px;background:var(--soft)}
.eyebrow{left:240px;top:605px;font-size:6.5px;color:var(--red)}
.sec-title{left:240px;top:615px;font-size:13.5px;font-weight:500;color:#333}
.arrows{left:704px;top:617px;display:flex;gap:3px}
.arrows span{width:12px;height:12px;border:1px solid #ddd;border-radius:50%;background:#fff}
.card{top:653px;width:107px;background:#fff;border:1px solid #eee}
.card .ph{height:102px}
.card .body{padding:5px 9px 8px;font-size:6.6px;color:#333}
.card .tags{color:var(--navy);font-size:6.3px;margin-top:2px;line-height:10px}
.card .meta{font-size:6px;color:#999;margin-top:7px}

/* lead engineer */
.lead-name{left:240px;top:830px;font-size:15px;font-weight:500;color:var(--navy)}
.lead-sub{left:240px;top:854px;width:330px;font-size:9.5px;font-weight:300;line-height:13px;color:#444}
.lead-text{left:240px;top:904px;width:150px;font-size:6.3px;line-height:10px;color:var(--muted)}
.skill{left:411px;width:151px;font-size:6.8px;color:#333}
.skill .top{display:flex;justify-content:space-between;padding-right:30px}
.skill .track{margin-top:6px;height:2px;background:#eee}
.skill .fill{height:2px;background:linear-gradient(90deg,var(--navy),var(--cyan))}
.lead-photo{left:615px;top:843px;width:165px;height:195px;background:linear-gradient(180deg,#eef2f6 0%,#dfe6ee 100%)}

/* footer */
.footer{left:133px;top:1038px;width:705px;height:162px;background:var(--foot)}
.fcol{top:1058px;width:107px;color:var(--foot-text);font-size:6.5px}
.fcol h5{font-size:8.5px;font-weight:500;color:#fff;padding-bottom:7px;position:relative;margin-bottom:14px}
.fcol h5:after{content:"";position:absolute;left:0;bottom:0;width:25px;height:1px;background:var(--red)}
.fcol li{list-style:none;border-bottom:1px solid var(--foot-line);padding:0 0 5px;margin-bottom:8px;line-height:9px}
.fcol li:last-child{border:0}
</style>
</head>
<body>

<div class="abs topbar">
  <div class="info-line">
    <svg width="7" height="9" viewBox="0 0 7 9"><path d="M3.5 8.5C1 5.5.5 4.5.5 3.3a3 3 0 0 1 6 0c0 1.2-.5 2.2-3 5.2z" fill="none" stroke="#ec1f27" stroke-width=".8"/></svg>
    <span>Fenwick Hollow, NY 10482, United States</span>
    <span class="gap"></span>
    <svg width="9" height="7" viewBox="0 0 9 7"><rect x=".5" y=".5" width="8" height="6" fill="none" stroke="#ec1f27" stroke-width=".8"/><path d="M.5.5l4 3 4-3" fill="none" stroke="#ec1f27" stroke-width=".8"/></svg>
    <span>hello@brimvale-oralnet.com</span>
  </div>
  <div class="socials"><i></i><i></i><i></i><i></i></div>
</div>

<div class="abs brand tech"><i></i>Brimvale OralNet IT</div>
<div class="abs call">
  <svg width="7" height="12" viewBox="0 0 7 12"><rect x=".5" y=".5" width="6" height="11" rx="1" fill="none" stroke="#ec1f27"/></svg>Call Us: 1-800-555-0142
</div>
<svg class="abs" style="left:720px;top:36px" width="14" height="14" viewBox="0 0 14 14"><circle cx="6" cy="6" r="4.8" fill="none" stroke="#0255a3" stroke-width="1.1"/><path d="M9.5 9.5L13 13M4 6h4M6 4v4" stroke="#0255a3" stroke-width="1.1"/></svg>
<div class="abs header-rule"></div>

<nav class="abs tabs" role="tablist">
  <span class="tab on" role="tab" aria-selected="true">Home</span>
  <span class="tab" role="tab">Services</span>
  <span class="tab" role="tab">Cloud</span>
  <span class="tab" role="tab">Support</span>
  <span class="tab" role="tab">Contacts</span>
</nav>

<section class="abs hero"><div class="grid-lines"></div></section>
<div class="abs hero-visual" role="img" aria-label="Network equipment in a modern dental office"></div>
<div class="abs hero-copy">
  <div class="kicker tech">Welcome to Brimvale OralNet IT</div>
  <div class="hl tech">Smart technology built</div><br>
  <div class="hl tech">for dental practices!</div>
  <p>Networks, cloud backup and audio visual systems.<br>Managed support for busy dental offices.</p>
  <div class="btns"><span class="btn fill">Get Support</span><span class="btn">Learn More</span></div>
</div>

<div class="abs feature" style="left:238px">
  <svg width="30" height="30" viewBox="0 0 30 30"><rect x="5" y="5" width="20" height="6" rx="1" fill="none" stroke="#0255a3"/><rect x="5" y="14" width="20" height="6" rx="1" fill="none" stroke="#0255a3"/><circle cx="9" cy="8" r="1" fill="#ec1f27"/><circle cx="9" cy="17" r="1" fill="#ec1f27"/><path d="M15 20v5M9 25h12" stroke="#0255a3"/></svg>
  <h3 class="tech">Computer Networks</h3>
  <p>Design, installation and upkeep of secure networks for every chair and front desk.</p>
</div>
<div class="abs feature" style="left:366px">
  <svg width="30" height="30" viewBox="0 0 30 30"><path d="M9 21h13a5 5 0 0 0 0-10 7 7 0 0 0-13-1 5.5 5.5 0 0 0 0 11z" fill="none" stroke="#0255a3"/><path d="M15 13v6M12 16l3 3 3-3" fill="none" stroke="#ec1f27"/></svg>
  <h3 class="tech">Cloud Backup</h3>
  <p>Automatic offsite data backup and a secure data center keep patient records safe.</p>
</div>
<div class="abs feature" style="left:495px">
  <svg width="30" height="30" viewBox="0 0 30 30"><rect x="4" y="6" width="22" height="14" rx="1" fill="none" stroke="#0255a3"/><path d="M13 10v6l5-3z" fill="#ec1f27"/><path d="M11 24h8M15 20v4" stroke="#0255a3"/></svg>
  <h3 class="tech">Audio Visual</h3>
  <p>Operatory screens, patient education displays and sound for a modern office.</p>
</div>
<div class="abs feature" style="left:623px">
  <svg width="30" height="30" viewBox="0 0 30 30"><path d="M6 16v-2a9 9 0 0 1 18 0v2" fill="none" stroke="#0255a3"/><rect x="4" y="15" width="4" height="7" rx="1" fill="none" stroke="#0255a3"/><rect x="22" y="15" width="4" height="7" rx="1" fill="none" stroke="#0255a3"/><path d="M24 22c0 3-3 4-7 4" fill="none" stroke="#ec1f27"/></svg>
  <h3 class="tech">Managed Support</h3>
  <p>Monitoring, help desk and on-site service so your team can focus on patients.</p>
</div>

<section class="abs info">
  <div class="news"><h4 class="tech">Tech News</h4>New cloud backup plans now cover imaging files and practice software databases.<br><br>Read more</div>
  <div class="hours"><h4 class="tech">Support Hours</h4>
    <div class="row"><span>Monday - Friday</span><span>8.00 - 17.00</span></div>
    <div class="row"><span>Saturday</span><span>9.30 - 17.30</span></div>
    <div class="row" style="border:0"><span>Sunday</span><span>9.30 - 15.00</span></div>
  </div>
  <div class="book"><h4 class="tech">Request Service</h4>
    <div class="form">
      <div class="field sel">Service Type</div><div class="field">Name</div>
      <div class="field">Phone</div><div class="field">Email</div>
      <div class="field">Date</div><div class="send">Send Request</div>
    </div>
  </div>
</section>

<section class="abs services"></section>
<div class="abs eyebrow">What We Do</div>
<h2 class="abs sec-title tech">Our Services</h2>
<div class="abs arrows"><span></span><span></span></div>

<article class="abs card" style="left:240px"><div class="ph" role="img" aria-label="Server rack with network cables" style="background:linear-gradient(135deg,#0a6fbf,#0255a3)"></div><div class="body">Network Installation<div class="tags">Networks, Hardware</div><div class="meta">○ 0 &nbsp; ♡ 39</div></div></article>
<article class="abs card" style="left:369px"><div class="ph" role="img" aria-label="Cloud storage dashboard on a screen" style="background:linear-gradient(135deg,#e6edf4,#c3d2e2)"></div><div class="body">Cloud Data Backup<div class="tags">Cloud, Data Center</div><div class="meta">○ 0 &nbsp; ♡ 29</div></div></article>
<article class="abs card" style="left:498px"><div class="ph" role="img" aria-label="Display screen in a dental operatory" style="background:linear-gradient(135deg,#dfe6ea,#b4c4d0)"></div><div class="body">Practice Audio Visual<div class="tags">Audio Visual, Displays</div><div class="meta">○ 0 &nbsp; ♡ 16</div></div></article>
<article class="abs card" style="left:626px"><div class="ph" role="img" aria-label="Technician at a help desk" style="background:linear-gradient(135deg,#e4e8ec,#b9c3cd)"></div><div class="body">Managed IT Support<div class="tags">Support, Monitoring</div><div class="meta">○ 0 &nbsp; ♡ 9</div></div></article>

<h2 class="abs lead-name tech">Lena Marsh, Lead Engineer</h2>
<p class="abs lead-sub">We are proud to keep your practice connected, protected and running every day</p>
<p class="abs lead-text">Our engineers know dental software, imaging and compliance. We plan, install and look after every part of your office technology, from the front desk to the sterilization room. Each system is monitored around the clock, backed up to our data center and supported by a team that answers quickly. Fewer outages mean more time for your patients and less time on hold.</p>
<div class="abs skill" style="top:907px"><div class="top"><span>Networks</span><span>78%</span></div><div class="track"><div class="fill" style="width:78%"></div></div></div>
<div class="abs skill" style="top:932px"><div class="top"><span>Cloud Backup</span><span>86%</span></div><div class="track"><div class="fill" style="width:86%"></div></div></div>
<div class="abs skill" style="top:957px"><div class="top"><span>Audio Visual</span><span>86%</span></div><div class="track"><div class="fill" style="width:86%"></div></div></div>
<div class="abs lead-photo" role="img" aria-label="Lead engineer holding a tablet"></div>

<footer class="abs footer"></footer>
<div class="abs fcol" style="left:240px"><h5 class="tech">Socials</h5><ul><li>Newsletter</li><li>Photo Feed</li><li>Updates</li><li>Video Channel</li></ul></div>
<div class="abs fcol" style="left:369px"><h5 class="tech">Our Team</h5><ul><li>Owen Calder</li><li>Ruth Penning</li><li>Milo Fenner</li><li>Iris Wexley</li></ul></div>
<div class="abs fcol" style="left:497px"><h5 class="tech">About Us</h5><ul><li>Services</li><li>Cloud Plans</li><li>Special Offers</li><li>FAQ</li></ul></div>
<div class="abs fcol" style="left:625px"><h5 class="tech">Contact</h5><ul><li>Fenwick Hollow, NY 10482, United States</li><li>Phone: 1-800-555-0142</li><li>Email: hello@brimvale-oralnet.com</li></ul></div>

</body>
</html>
```